Web-Design for Electrcian Company

Our Customer is a small business electrian in Switzerland. He is looking for a fresh and innovative website design. He is well known for his extra service, and that they always go for the extra-mile! In his logo you also see that positive and fresh image the try to bring to the customer. the main colors are black, red and white.

the website structure will be:

- home
- services (with submenu for each service)
- references (with submenu for each category of services)
- about us (2 submenus: history and staff)
- links
- Contact

Target Market(s)

Architects, building owners, people from the age of 35 up...

Industry/Entity Type

Small Business

```html
<!DOCTYPE html>
<html lang="en">
<head>
<meta charset="utf-8">
<title>Brunner + Weiss Elektro AG – Home</title>
<link rel="stylesheet" href="https://fonts.googleapis.com/css2?family=Arimo:ital,wght@0,400;0,700;1,400;1,700&family=Open+Sans:ital,wght@0,400;0,700;0,800;1,600&family=Questrial&display=swap">
<style>
  :root {
    --black: #000;
    --white: #fff;
    --red: #e0262e;
    --text: #333;
    --muted: #555;
    --heading-grey: #6f6f6f;
    --rule: #dcdcdc;
    --frame: #dde1ea;
    --sky: #b6dcf6;
    --link-blue: #4f8fe6;
    --orange: #f0642a;
    --footer-rule: #333;
  }
  * { box-sizing: border-box; margin: 0; padding: 0; }
  html, body { width: 1022px; height: 1200px; overflow: hidden; background: var(--white); }
  body { position: relative; font-family: "Arimo", Arial, sans-serif; color: var(--text); }
  .abs { position: absolute; }
  h1, h2, h3 { font-weight: 400; }

  .top-bar { left: 0; top: 0; width: 1022px; height: 10px; background: #111; }
  .top-line { left: 0; top: 14px; width: 1022px; height: 3px; background: #e8e8e8; }

  .brand-name { left: 40px; top: 40px; font-family: "Open Sans", sans-serif; font-weight: 700; font-size: 25px; line-height: 34px; color: var(--black); }

  .main-nav { top: 71px; right: 41px; display: flex; gap: 34px; font-size: 14px; }
  .main-nav a { color: var(--black); text-decoration: none; letter-spacing: .2px; }
  .main-nav a.active { color: var(--red); }

  .hero-frame { left: 34px; top: 140px; width: 950px; height: 340px; background: var(--frame); box-shadow: 0 8px 8px -4px rgba(0,0,0,.22); }
  .hero-image { left: 44px; top: 150px; width: 930px; height: 320px; overflow: hidden;
    background: linear-gradient(100deg, #cbb8d6 0%, #c4acd2 45%, #8e5bc2 62%, #c9a6dd 80%, #dbc3e8 100%); }
  .hero-rule { left: 0; width: 930px; height: 1px; background: rgba(255,255,255,.85); }
  .hero-kicker { left: 52px; top: 94px; font-family: "Open Sans", sans-serif; font-size: 32px; color: var(--sky); letter-spacing: -.5px; }
  .hero-title { left: 50px; top: 124px; font-family: "Open Sans", sans-serif; font-weight: 800; font-size: 68px; color: var(--white); letter-spacing: -1.5px; text-shadow: 3px 4px 6px rgba(0,0,0,.4); }

  .col-rule { top: 525px; width: 1px; height: 368px; background: var(--rule); }
  .section-title { font-family: "Questrial", sans-serif; font-size: 32px; color: var(--heading-grey); }
  .welcome-title { left: 24px; top: 520px; color: var(--red); font-size: 36px; }

  .map-box { left: 24px; top: 591px; width: 342px; height: 166px; border-radius: 6px; background: #fff; border: 1px solid #ccc; box-shadow: 2px 3px 4px rgba(0,0,0,.3); padding: 5px; }
  .map-fill { width: 100%; height: 100%; background: radial-gradient(ellipse at 45% 50%, #3a5ea5 0%, #c9cfd8 70%, #e6e8eb 100%); }

  .body-copy { font-size: 13.5px; line-height: 16.5px; color: var(--muted); }
  .welcome-copy { left: 24px; top: 777px; width: 346px; }

  .btn { display: inline-block; font-weight: 700; font-size: 13.5px; color: var(--white); text-align: center; border-radius: 4px; }
  .btn-red { left: 26px; top: 871px; width: 90px; height: 23px; line-height: 23px; background: linear-gradient(#ef3a3a, #c81e22); box-shadow: 0 0 0 1px #f4a0a0; }
  .btn-dark { left: 455px; top: 866px; width: 111px; height: 24px; line-height: 22px; background: linear-gradient(#5a5a5a, #3c3c3c); border: 1px solid #222; }

  .news-item { left: 454px; width: 224px; }
  .news-date { font-size: 13px; color: var(--black); border-bottom: 1px solid var(--black); display: inline-block; padding-bottom: 1px; }
  .news-item .body-copy { margin-top: 10px; padding-left: 1px; }
  .more-link { margin-top: 14px; font-size: 13px; color: var(--black); }

  .popular-item { left: 762px; width: 230px; }
  .popular-head { display: flex; align-items: center; gap: 8px; font-weight: 700; font-size: 13.5px; color: var(--red); }
  .popular-item .body-copy { margin-top: 7px; padding-left: 20px; }

  .footer { left: 0; top: 940px; width: 1022px; height: 260px; background: var(--black); color: var(--white); }
  .footer-rule { top: 30px; width: 1px; height: 145px; background: var(--footer-rule); }
  .clients-title { left: 28px; top: 42px; font-family: "Questrial", sans-serif; font-size: 24px; letter-spacing: 1px; }
  .testimonial { left: 91px; top: 80px; font-family: "Open Sans", sans-serif; font-style: italic; font-weight: 600; font-size: 12px; line-height: 19.5px; }
  .testimonial-author { right: 622px; top: 140px; font-size: 13px; }
  .testimonial-author span { color: var(--link-blue); }
  .newsletter-title { left: 453px; top: 40px; font-family: "Questrial", sans-serif; font-size: 26px; letter-spacing: .5px; }
  .email-field { left: 453px; top: 91px; width: 227px; height: 26px; border-radius: 4px; background: #3c3c3c; border: 1px solid #5c5c5c; font-size: 13px; line-height: 24px; padding-left: 10px; color: #eee; }
  .subscribe-btn { left: 591px; top: 125px; width: 88px; height: 22px; border-radius: 3px; background: linear-gradient(#fff, #cfcfcf); color: var(--black); font-size: 13.5px; line-height: 22px; text-align: center; }
  .address { left: 763px; top: 45px; font-family: "Open Sans", sans-serif; font-style: italic; font-weight: 600; font-size: 12.5px; line-height: 22px; }
  .footer-bar { left: 23px; top: 204px; width: 967px; height: 7px; border-radius: 4px; background: linear-gradient(#777, #3a3a3a); }
  .copyright { left: 27px; top: 225px; font-size: 13.5px; }
</style>
</head>
<body>
  <div class="abs top-bar"></div>
  <div class="abs top-line"></div>

  <header>
    <div class="abs brand-name">Brunner + Weiss<br>Elektro AG</div>
    <nav class="abs main-nav">
      <a class="active" href="#">HOME</a>
      <a href="#">SERVICES</a>
      <a href="#">REFERENCES</a>
      <a href="#">ABOUT US</a>
      <a href="#">LINKS</a>
      <a href="#">CONTACT</a>
    </nav>
  </header>

  <section>
    <div class="abs hero-frame"></div>
    <div class="abs hero-image" role="img" aria-label="Photo of modern purple interior with round pendant lights">
      <div class="abs hero-rule" style="top:78px"></div>
      <div class="abs hero-rule" style="top:214px"></div>
      <div class="abs hero-kicker">BRUNNER + WEISS ELEKTRO AG</div>
      <div class="abs hero-title">Modern Lightning</div>
    </div>
  </section>

  <main>
    <div class="abs col-rule" style="left:414px"></div>
    <div class="abs col-rule" style="left:722px"></div>

    <h1 class="abs section-title welcome-title">Welcome!</h1>
    <div class="abs map-box"><div class="map-fill" role="img" aria-label="World map illustration with connection points"></div></div>
    <p class="abs body-copy welcome-copy">Moleie lacneanrit maellus porase qus esedasese dusce lertswer lrurtasfeugiat malesuad asorbi nunogravida aturs usecuctu aecenas tristique orci ac semet rtertas dertas Uls pharetra ma onec accumsan.</p>
    <a class="abs btn btn-red">Read More</a>

    <h2 class="abs section-title" style="left:454px;top:523px">Latest News</h2>
    <div class="abs news-item" style="top:584px">
      <div class="news-date">22.10.12 Penatibu partus</div>
      <p class="body-copy">Monlase dusce hertse nem ipsumal Kaecenas tristique oasem. Duis ultric ies pharagna onec accumsa.</p>
      <div class="more-link">More News</div>
    </div>
    <div class="abs news-item" style="top:730px">
      <div class="news-date">14.10.12 Mertys letuiser tase</div>
      <p class="body-copy">Nem ipsumal bonlase dusce hertse que oasem. Duis ultriaecenas tristi ec accuies pharagna onmsa.</p>
      <div class="more-link">More News</div>
    </div>
    <a class="abs btn btn-dark">News Archive</a>

    <h2 class="abs section-title" style="left:761px;top:523px">Most Popular</h2>
    <div class="abs popular-item" style="top:590px">
      <div class="popular-head"><svg width="13" height="13" viewBox="0 0 13 13"><circle cx="6.5" cy="6.5" r="5.5" fill="none" stroke="var(--orange)" stroke-width="1.4"/><path d="M6.5 3.6v5.8M3.6 6.5h5.8" stroke="var(--orange)" stroke-width="1.6"/></svg>Lorem Ipsum</div>
      <p class="body-copy">Dalesuad asorbi nunra vidasea atcurs usecuctu.</p>
    </div>
    <div class="abs popular-item" style="top:667px">
      <div class="popular-head"><svg width="13" height="13" viewBox="0 0 13 13"><circle cx="6.5" cy="6.5" r="5.5" fill="none" stroke="var(--orange)" stroke-width="1.4"/><path d="M6.5 3.6v5.8M3.6 6.5h5.8" stroke="var(--orange)" stroke-width="1.6"/></svg>Lorem Ipsum</div>
      <p class="body-copy">Naser maellus pore qus esedas-esdusce lerts lrurtasfeu</p>
    </div>
    <div class="abs popular-item" style="top:744px">
      <div class="popular-head"><svg width="13" height="13" viewBox="0 0 13 13"><circle cx="6.5" cy="6.5" r="5.5" fill="none" stroke="var(--orange)" stroke-width="1.4"/><path d="M6.5 3.6v5.8M3.6 6.5h5.8" stroke="var(--orange)" stroke-width="1.6"/></svg>Lorem Ipsum</div>
      <p class="body-copy">Atcurs usuctu aecenas tristique Uls pharetra mec accumsan.</p>
    </div>
    <div class="abs popular-item" style="top:821px">
      <div class="popular-head"><svg width="13" height="13" viewBox="0 0 13 13"><circle cx="6.5" cy="6.5" r="5.5" fill="none" stroke="var(--orange)" stroke-width="1.4"/><path d="M6.5 3.6v5.8M3.6 6.5h5.8" stroke="var(--orange)" stroke-width="1.6"/></svg>Lorem Ipsum</div>
      <p class="body-copy" style="margin-top:10px">Merts maellrase qus esedasese dusceer lrurtasfeugiat.</p>
    </div>
  </main>

  <footer class="abs footer">
    <div class="abs footer-rule" style="left:414px"></div>
    <div class="abs footer-rule" style="left:722px"></div>

    <h3 class="abs clients-title">OUR CLIENTS SAY:</h3>
    <blockquote class="abs testimonial">Atcurs usuctu aecenas tristique<br>Ulspharetra mec accumsan kertrertase<br>Malesuada nec sit ametem ipsum</blockquote>
    <div class="abs testimonial-author"><span>John Doe</span>, ABC Company Inc.</div>

    <h3 class="abs newsletter-title">Newsletter</h3>
    <div class="abs email-field">enter your - mail</div>
    <div class="abs subscribe-btn">Subscribe</div>

    <address class="abs address">Brunner + Weiss Elektro AG,<br>99 Some Street, 12345 Some City,<br>Switzerland</address>

    <div class="abs footer-bar"></div>
    <div class="abs copyright">Brunner + Weiss Elektro AG © 2012|All Rights Reserved</div>
  </footer>
</body>
</html>
```